Merchandising für Schülermarketing
Zielgruppe
FALDO Cash & Carry gibt es bereits seit 1964. Die FALDO Cash & Carry Deutschland GmbH zählt national und international zu den Marktführern im Großhandel und betreibt mit den Marken FALDO und V+V BRÜNDEL 107 Cash & Carry Märkte in Deutschland mit mehr als 17.000 Mitarbeitern. Wir haben 50.000 Artikel im Sortiment und bedienen damit Kunden aus Gastronomie, Hotellerie, Kiosken, Tankstellen, Vereinen, Freiberuflern, etc.
Für unsere Ausbildungsberufe in den Großmärkten (insbes. Kaufmann im Groß- und Außenhandel, Verkäufer, Einzelhandelskaufmann, Fachkraft für Lagerlogistik) suchen wir deutschlandweit viele Azubis. Zielgruppe sind Schüler mit mind. Realschulabschluss.
Aufgabenstellung
Deutschlandweit nehmen wir für das Azubimarketing auf verschiedenen Recruitingmessen teil. Dort verteilen wir Infomaterial aber auch Giveaways. Die Giveaways aktualisieren wir derzeit (Kulis, Textmarker in blau & gelb, faltbarer Einkaufsbeutel mit Logo). Neu dazu soll ein Jutebeutel für die Zielgruppe Schüler kommen, für den wir ein Design suchen.
Der Beutel soll das aktuelle Firmenlogo sichtbar tragen, aber dennoch optisch für die junge Zielgruppe ansprechend sein, so dass er regelmäßig genutzt wird. Gern kann das Design einen grafischen Aufdruck beinhalten oder einen witzigen Spruch, der irgendwie mit Arbeiten bei Faldo in Zusammenhang steht.

```html
<!DOCTYPE html>
<html lang="de">
<head>
<meta charset="utf-8">
<title>Jutebeutel – FALDO Azubimarketing</title>
<link rel="stylesheet" href="https://fonts.googleapis.com/css2?family=Montserrat:wght@800&family=Kaushan+Script&display=swap">
<style>
  :root {
    --bag-white: #ffffff;
    --print-black: #0d0d0d;
  }
  html, body {
    margin: 0;
    padding: 0;
    width: 815px;
    height: 1200px;
    overflow: hidden;
    background: var(--bag-white);
  }
  .bag-print {
    position: relative;
    width: 815px;
    height: 1200px;
    background: var(--bag-white);
    color: var(--print-black);
  }
  .bag-print > * {
    position: absolute;
    left: 0;
    width: 100%;
    margin: 0;
    text-align: center;
    white-space: nowrap;
  }
  .headline-big {
    font-family: "Montserrat", "Arial Black", sans-serif;
    font-weight: 800;
    line-height: 1;
    letter-spacing: -0.01em;
  }
  .headline-jut {
    top: 176px;
    font-size: 262px;
  }
  .slogan-script {
    top: 446px;
    font-family: "Kaushan Script", cursive;
    font-size: 72px;
    line-height: 80px;
    letter-spacing: 2px;
    word-spacing: 8px;
  }
  .headline-beutel {
    top: 628px;
    font-size: 126px;
  }
  .brand-name {
    top: 1010px;
    font-family: "Montserrat", "Arial Black", sans-serif;
    font-weight: 800;
    font-size: 92px;
    line-height: 1;
    letter-spacing: 0.01em;
  }
</style>
</head>
<body>
  <main class="bag-print">
    <h1 class="headline-big headline-jut">JUT</h1>
    <p class="slogan-script">sind bei uns<br>nicht nur die</p>
    <p class="headline-big headline-beutel">BEUTEL</p>
    <p class="brand-name">FALDO</p>
  </main>
</body>
</html>
```